Redesign of Medical App for Patients

• The Designer’s task is to provide a new fully-responsive design for our apps, and then code it using only basic html and CSS.
• Your design will be incorporated into our existing REACT native app.

Target Market(s)

Medical Patients

Industry/Entity Type

Medical

Coding

Coded - Design and coding required

Number of Pages Required

5+ page

Requirements
Must have
• Short list candidates will receive detailed briefing
Nice to have
• detailed briefing contains some of our ideas.

```html
<!DOCTYPE html>
<html lang="en">
<head>
<meta charset="utf-8">
<title>CareSteps – Patient App Screens</title>
<link rel="stylesheet" href="https://fonts.googleapis.com/css2?family=Open+Sans:wght@400;600;700&family=Roboto+Condensed:wght@700&display=swap">
<style>
:root{
  --bg-1:#1f7fc4;
  --bg-2:#2fb3e6;
  --screen:#eef6fc;
  --header-top:#d6ecfa;
  --brand:#0f5aa6;
  --brand-dark:#0b4d8f;
  --accent:#1b8fd6;
  --ink:#2b3440;
  --muted:#555f6b;
  --card:#ffffff;
  --row:#eef1f4;
  --panel:#f1f3f5;
}
*{box-sizing:border-box;margin:0;padding:0}
html,body{width:1200px;height:874px;overflow:hidden}
body{
  font-family:"Open Sans",sans-serif;
  background:linear-gradient(135deg,var(--bg-1),var(--bg-2));
  position:relative;color:var(--ink);
}
.screen{
  position:absolute;top:98px;width:300px;height:680px;
  background:var(--screen);border-radius:26px;overflow:hidden;
  box-shadow:0 10px 30px rgba(0,40,90,.25);
}
.screen--home{left:68px}
.screen--procedures{left:450px}
.screen--recovery{left:832px}

.app-header{
  height:86px;padding:40px 16px 0;
  background:linear-gradient(180deg,var(--header-top),var(--screen));
  display:flex;align-items:flex-start;justify-content:space-between;
}
.icon-btn{
  width:16px;height:16px;border-radius:50%;background:#fff;
  display:flex;align-items:center;justify-content:center;
  box-shadow:0 1px 3px rgba(0,0,0,.15);margin-top:3px;
}
.brand{display:flex;align-items:center;gap:6px;
  font-size:16px;font-weight:600;color:var(--brand-dark);letter-spacing:.2px}
.brand__mark{width:20px;height:20px;border-radius:50%;background:var(--brand)}

/* home */
.diagram{
  margin:4px 17px 0;height:175px;border-radius:8px;
  background:radial-gradient(ellipse at 45% 45%,#b8403a 0 30%,#7d2422 45%,#fff 62%);
  box-shadow:0 2px 8px rgba(0,40,90,.12);
}
.topic-grid{
  margin:20px 18px 0;display:grid;grid-template-columns:1fr 1fr;gap:16px 12px;
}
.topic{
  background:var(--card);border-radius:3px;height:100px;padding:9px 9px 0;position:relative;
  box-shadow:0 1px 4px rgba(0,40,90,.08);
}
.topic--active{background:var(--brand);color:#fff}
.topic__badge{position:absolute;right:8px;top:10px;width:18px;height:18px;border-radius:50%;background:var(--brand);border:2px solid #fff;box-shadow:0 0 0 1px var(--brand)}
.topic--active .topic__badge{display:none}
.topic__title{font-size:6.4px;font-weight:700;line-height:1.9;color:var(--brand-dark);padding-right:22px}
.topic--active .topic__title{color:#fff}
.topic__text{font-size:5.6px;line-height:2.1;color:var(--muted);margin-top:2px}
.topic--active .topic__text{color:#e4f0fb}
.topic__link{font-size:6px;color:var(--brand);position:absolute;bottom:9px;left:9px}
.topic--active .topic__link{color:#fff;font-weight:700}
.footer-brand{position:absolute;bottom:14px;left:0;right:0;display:flex;justify-content:center}

/* section screens */
.pill{
  display:block;width:max-content;margin:-4px auto 0;padding:3px 17px;border-radius:14px;
  background:var(--brand);color:#fff;font-family:"Roboto Condensed",sans-serif;
  font-size:13px;letter-spacing:.3px;
}
.photo{
  margin:6px 14px 0;height:168px;border-radius:10px;
  box-shadow:0 4px 10px rgba(0,40,90,.2);
}
.photo--team{background:linear-gradient(180deg,#e6ecf1,#8fb8dc 60%,#3f86c4)}
.photo--consult{background:linear-gradient(90deg,#4d7fb8,#e8e3dc 55%,#9aa0a6)}
.panel{
  margin:14px 14px 0;background:#fff;border-radius:8px;padding:9px 8px 12px;
}
.accordion{list-style:none}
.acc-row{
  height:21px;background:var(--row);margin-bottom:6px;padding:0 9px;
  display:flex;align-items:center;justify-content:space-between;
  font-size:7.8px;color:var(--ink);
}
.acc-row--open{background:var(--brand);color:#fff;margin-bottom:0}
.chev{width:10px;height:10px;border-radius:50%;background:#111;display:flex;align-items:center;justify-content:center}
.acc-row--open .chev{background:#fff}
.acc-body{background:var(--panel);padding:8px 9px 10px;margin-bottom:8px}
.acc-body p{font-size:5.8px;line-height:2.1;color:var(--muted);margin-bottom:4px}
.acc-body a{font-size:6.2px;color:var(--brand);text-decoration:none}
.procedure-image{height:68px;background:linear-gradient(90deg,#6a2a2a,#a54a3a 50%,#d9b8bd);margin-bottom:10px}
</style>
</head>
<body>

<svg width="0" height="0" style="position:absolute">
  <defs>
    <symbol id="chev-down" viewBox="0 0 10 10"><path d="M3 4l2 2 2-2" fill="none" stroke="#fff" stroke-width="1.3"/></symbol>
    <symbol id="chev-up" viewBox="0 0 10 10"><path d="M3 6l2-2 2 2" fill="none" stroke="#0f5aa6" stroke-width="1.3"/></symbol>
    <symbol id="menu" viewBox="0 0 10 10"><path d="M2.5 3h5M2.5 5h4M2.5 7h3" stroke="#0f5aa6" stroke-width="1"/></symbol>
    <symbol id="next" viewBox="0 0 10 10"><path d="M4 3l2 2-2 2" fill="none" stroke="#9bb" stroke-width="1"/></symbol>
  </defs>
</svg>

<!-- Home -->
<section class="screen screen--home">
  <header class="app-header">
    <span class="icon-btn"><svg width="10" height="10"><use href="#menu"/></svg></span>
    <span class="brand"><span class="brand__mark"></span>CARESTEPS</span>
    <span class="icon-btn"><svg width="10" height="10"><use href="#next"/></svg></span>
  </header>
  <div class="diagram" role="img" aria-label="Labelled anatomy illustration of the liver, gall bladder and bile duct"></div>
  <div class="topic-grid">
    <article class="topic"><span class="topic__badge"></span>
      <h3 class="topic__title">Is it too late to prevent gall bladder disease?</h3>
      <p class="topic__text">Yes, unfortunately. If you have symptomatic gallbladder disease, surgery is the most likely solution.</p>
      <span class="topic__link">Read More</span></article>
    <article class="topic topic--active"><span class="topic__badge"></span>
      <h3 class="topic__title">What will happen if I don't have this procedure?</h3>
      <p class="topic__text">If you chose not to undergo surgery – and do not adopt other solutions - it is likely that your pain</p>
      <span class="topic__link">Read More &rarr;</span></article>
    <article class="topic"><span class="topic__badge"></span>
      <h3 class="topic__title">Are there alternative solutions?</h3>
      <p class="topic__text">If you are suffering from gallbladder disease and are a strong surgical candidate, you</p>
      <span class="topic__link">Read More</span></article>
    <article class="topic"><span class="topic__badge"></span>
      <h3 class="topic__title">What are the risks of this procedure?</h3>
      <p class="topic__text">All procedures have risks, but this is usually a straightforward procedure.</p>
      <span class="topic__link">Read More</span></article>
    <article class="topic"><span class="topic__badge"></span>
      <h3 class="topic__title">Are there alternative solutions?</h3>
      <p class="topic__text">If you are suffering from gallbladder disease and are a strong surgical candidate, you</p>
      <span class="topic__link">Read More</span></article>
    <article class="topic"><span class="topic__badge"></span>
      <h3 class="topic__title">What are the risks of this procedure?</h3>
      <p class="topic__text">All procedures have risks, but this is usually a straightforward procedure.</p>
      <span class="topic__link">Read More</span></article>
  </div>
  <footer class="footer-brand"><span class="brand"><span class="brand__mark"></span>CARESTEPS</span></footer>
</section>

<!-- Procedures -->
<section class="screen screen--procedures">
  <header class="app-header">
    <span class="icon-btn"><svg width="10" height="10"><use href="#menu"/></svg></span>
    <span class="brand"><span class="brand__mark"></span>CARESTEPS</span>
    <span class="icon-btn"><svg width="10" height="10"><use href="#next"/></svg></span>
  </header>
  <span class="pill">PROCEDURES</span>
  <div class="photo photo--team" role="img" aria-label="Photo of a smiling medical team in scrubs and white coats"></div>
  <div class="panel">
    <ul class="accordion">
      <li class="acc-row">Preparation<span class="chev"><svg width="10" height="10"><use href="#chev-down"/></svg></span></li>
      <li class="acc-row acc-row--open">What happens?<span class="chev"><svg width="10" height="10"><use href="#chev-up"/></svg></span></li>
      <li class="acc-body">
        <div class="procedure-image" role="img" aria-label="Close-up photo of liver tissue during a surgical procedure"></div>
        <p>Just prior to your operation, you will undergo general anesthesia and have a breathing tube, otherwise known as an endotracheal tube, placed down your throat (i.e. intubation). Your breathing tube will most likely be removed by the time you wake up from your surgery.</p>
        <a href="#">Read More</a>
      </li>
      <li class="acc-row">Preparation<span class="chev"><svg width="10" height="10"><use href="#chev-down"/></svg></span></li>
      <li class="acc-row">When do I leave the Hospital?<span class="chev"><svg width="10" height="10"><use href="#chev-down"/></svg></span></li>
      <li class="acc-row">Waking Up<span class="chev"><svg width="10" height="10"><use href="#chev-down"/></svg></span></li>
      <li class="acc-row">Pain management<span class="chev"><svg width="10" height="10"><use href="#chev-down"/></svg></span></li>
      <li class="acc-row">Same-day Discharge<span class="chev"><svg width="10" height="10"><use href="#chev-down"/></svg></span></li>
    </ul>
  </div>
</section>

<!-- Recovery -->
<section class="screen screen--recovery">
  <header class="app-header">
    <span class="icon-btn"><svg width="10" height="10"><use href="#menu"/></svg></span>
    <span class="brand"><span class="brand__mark"></span>CARESTEPS</span>
    <span class="icon-btn"><svg width="10" height="10"><use href="#next"/></svg></span>
  </header>
  <span class="pill">RECOVERY</span>
  <div class="photo photo--consult" role="img" aria-label="Photo of a doctor in scrubs talking with a patient"></div>
  <div class="panel">
    <ul class="accordion">
      <li class="acc-row">When do I leave the Hospital?<span class="chev"><svg width="10" height="10"><use href="#chev-down"/></svg></span></li>
      <li class="acc-row">Waking Up<span class="chev"><svg width="10" height="10"><use href="#chev-down"/></svg></span></li>
      <li class="acc-row">Pain management<span class="chev"><svg width="10" height="10"><use href="#chev-down"/></svg></span></li>
      <li class="acc-row">Same-day Discharge<span class="chev"><svg width="10" height="10"><use href="#chev-down"/></svg></span></li>
      <li class="acc-row acc-row--open">Ready to leave<span class="chev"><svg width="10" height="10"><use href="#chev-up"/></svg></span></li>
      <li class="acc-body">
        <p>We encourage you to not expect too much from yourself as you recover.</p>
        <p>Please make sure you have a responsible adult to drive you home. You will not be allowed to leave the hospital on your own. It is also encouraged to have a responsible adult stay with you for 24 hours after your surgery to observe you</p>
        <a href="#">Read More</a>
      </li>
      <li class="acc-row">Sex when we have<span class="chev"><svg width="10" height="10"><use href="#chev-down"/></svg></span></li>
      <li class="acc-row">Return to Work<span class="chev"><svg width="10" height="10"><use href="#chev-down"/></svg></span></li>
      <li class="acc-row">When do I leave the Hospital?<span class="chev"><svg width="10" height="10"><use href="#chev-down"/></svg></span></li>
      <li class="acc-row">Waking Up<span class="chev"><svg width="10" height="10"><use href="#chev-down"/></svg></span></li>
    </ul>
  </div>
</section>

</body>
</html>
```